Cash Balance Retirement Plan Services Page

We are looking to have a services/landing page created for one of our offerings. The goal of the page is to explain a relatively complex service (advanced retirement plan) by highlighting the benefits and uses for the plan such that it tells a story that encourages individuals and businesses that would benefit from the plans to reach out.

The page will be used both as a landing page (though secondarily) and as a page that many of our partners will show to their clients in order to generate interest. We help other people closes these deals so we want it to handle both.

Overall, we would want the page to incorporate the following sections/areas.
1. Headline and a place for a video at the top
2. Explanation of what a cash balance plan is (a paragraph or two)
3. These five benefits: These are the 7 we usually use, but only include five at a time so only need room for five.
a. Highest Tax Deductible Contributions Allowed
b. Significantly reduce your taxes
c. Potential Negative “Net Cost”
d. Owner & Executive Weighted Benefits
e. Retain and Attract Top Talen
f. Catch Up On decades of low retirement savings in a matter of years
g. Potential for life time income
4. A section comparing the contribution limits allowed for each plan type (Please see attached image as an example).
5. A place for a table of contribution amounts (This will just be an image. Also, attached).
6. A place for a compare table
6. Who should consider such a plan
7. Occasional banners for call to actions
8. FAQ

Our primary audience for this project are successful small business owners with a particular focus on medical professionals (doctors, chiropractors, dentists, plastic surgeons, etc.). In generally, they will be between 45 and 65 years old and earn $150k or more.

Because we work a lot with financial, business strategy, and insurance based products that require a significant investment by the client trust, professionalism, and sophistication are important attributes we wish to portray in the design of the page. Our preferred colors are blue or green. Though we are still working on figuring out the color scheme so your input as a designer is welcomed as your creativity can help us communicate the attributes we seek to embody for our clients.

In the attached document, I have included some additional information about the service itself if it helps to have some context, as well as a more flushed out outline of the details above.

Importantly, I am not a marketer so any creative input is always welcome if there is a best practice we are not incorporating in either our design requests or outline.

Here is the URL for our current page: https://www.brightoakpartners.com/doctorcashplan

Please don't let this page be your muse. We're trying to get away from it for a reason :) But it still will hopefully provide some helpful information, copy examples, and context.

Additionally, please don't feel like you need to read the full cash balance explanation. That's only if context will be helpful.

We are also going through a rebranding so please don't rely on the colors from the BrightOakPartners logo you may see on the website. I've attached two sample logos for the rebrand for context.

```html
<!DOCTYPE html>
<html lang="en">
<head>
<meta charset="utf-8">
<title>Summit Ridge Financial — Retirement Plans</title>
<link href="https://fonts.googleapis.com/css2?family=Rubik:wght@500;700;800&family=Roboto+Condensed:wght@500&family=Mulish:wght@400;600;700&display=swap" rel="stylesheet">
<style>
:root{
  --navy:#0b2a55;
  --ink:#1c2331;
  --blue:#0a67d0;
  --sky:#18a6ea;
  --text:#3b4250;
  --hero-bg:#eef0f3;
  --dark:#040d24;
  --line:#e3e6ea;
  --star:#f3a81b;
}
*{box-sizing:border-box;margin:0;padding:0}
html,body{width:873px;height:1200px;overflow:hidden;background:#fff}
body{position:relative;font-family:"Mulish",sans-serif;color:var(--text)}
.abs{position:absolute}

.topbar{left:0;top:0;width:873px;height:29px;border-bottom:1px solid var(--line);font-size:8.5px}
.topbar .notice{left:58px;top:0;height:29px;width:310px;border-left:1px solid var(--line);border-right:1px solid var(--line);padding-left:12px;line-height:28px}
.topbar .notice b{color:var(--ink)}
.topbar .phone{left:686px;top:0;height:29px;width:133px;border-left:1px solid var(--line);text-align:right;line-height:28px}
.topbar .phone a{color:var(--ink);font-weight:700;text-decoration:underline}

.brand{left:62px;top:33px;height:46px;display:flex;align-items:center;gap:7px}
.brand .mark{width:44px;height:44px;border-radius:50%;background:var(--navy)}
.brand .name{font-family:"Rubik",sans-serif;font-weight:800;font-size:16px;line-height:16px;color:var(--navy);letter-spacing:.2px}
.nav{left:313px;top:49px;display:flex;gap:35px;font-family:"Rubik",sans-serif;font-weight:500;font-size:10.5px;color:var(--ink)}
.btn{display:flex;align-items:center;justify-content:center;gap:5px;font-family:"Rubik",sans-serif;font-weight:500;font-size:10.5px;color:#fff;background:var(--blue);border-radius:2px;white-space:nowrap}
.quote{left:712px;top:41px;width:107px;height:31px;background:linear-gradient(90deg,#0a67d0,#1496e6)}

.hero-bg{left:0;top:85px;width:873px;height:460px;background:var(--hero-bg)}
.hero-photo{left:360px;top:85px;width:513px;height:435px;background:linear-gradient(100deg,rgba(238,240,243,1) 0%,rgba(216,219,224,.9) 25%,#c9ccd3 60%,#b4b9c2 100%)}
.tagline{left:58px;top:135px;font-family:"Rubik",sans-serif;font-weight:500;font-size:11px;color:var(--blue)}
.tagline span{color:var(--sky)}
.headline{left:58px;top:170px;width:420px;color:var(--navy)}
.headline .lead{display:block;font-family:"Rubik",sans-serif;font-weight:800;font-size:32px;line-height:46px}
.headline .rest{display:block;font-family:"Roboto Condensed",sans-serif;font-weight:500;font-size:31px;line-height:48px}
.hero-copy{left:58px;top:329px;width:370px;font-size:13.5px;line-height:23px}
.cta1{left:58px;top:390px;width:102px;height:32px}
.cta2{left:166px;top:390px;width:139px;height:32px;background:#fff;color:var(--ink);border:1px solid #d7dbe1}
.rating{left:58px;top:430px;display:flex;gap:5px;align-items:center;font-size:8.5px}
.rating .stars{color:var(--star);font-size:9px;letter-spacing:-1px}
.play{left:601px;top:281px;width:68px;height:68px}

.card{background:#fff;box-shadow:0 4px 16px rgba(0,0,0,.08);padding:5px}
.card .img{width:100%;height:100%}
.card .icon{position:absolute;right:5px;bottom:5px;width:52px;height:52px;background:var(--blue);display:flex;align-items:center;justify-content:center}
.c1{left:58px;top:520px;width:180px;height:180px}
.c2{left:258px;top:520px;width:180px;height:180px}
.c3{left:457px;top:520px;width:360px;height:180px;display:flex}
.c3 .img{width:170px}
.c3 .icon{left:123px;top:64px;right:auto;bottom:auto}
.c3 .panel{flex:1;background:var(--dark);padding:18px 14px;color:#b9c0cf}
.c3 h3{font-family:"Rubik",sans-serif;font-weight:700;color:#fff;font-size:14.5px;line-height:19.5px;margin-bottom:10px}
.c3 p{font-size:9.5px;line-height:15.5px;margin-bottom:14px}
.c3 .link{font-family:"Rubik",sans-serif;font-weight:500;font-size:9.5px;color:#fff}
.c3 .link span{color:var(--sky)}

.rule{left:58px;top:776px;width:30px;height:3px;background:linear-gradient(90deg,var(--blue),var(--sky));border-radius:2px}
.savings-title{left:58px;top:788px;width:440px;color:var(--navy);font-weight:500;font-family:"Roboto Condensed",sans-serif;font-size:31px;line-height:33px}
.savings-title b{font-family:"Rubik",sans-serif;font-weight:800}
.intro{left:58px;top:869px;width:430px;font-size:11.5px;line-height:21px;color:var(--ink)}
.feature{top:955px;width:140px}
.feature .ico{display:block;width:32px;height:34px;margin-bottom:14px}
.feature h4{font-family:"Rubik",sans-serif;font-weight:700;font-size:13px;color:var(--ink);margin-bottom:7px}
.feature p{font-size:9.6px;line-height:15.5px;color:var(--ink);width:134px}
.f1{left:58px}.f2{left:222px}.f3{left:386px}
.services{left:58px;top:1092px;width:107px;height:31px}
.frame{left:487px;top:786px;width:332px;height:325px}
</style>
</head>
<body>

<div class="abs topbar">
  <div class="abs notice"><b>COVID-19:</b>We're providing a 15% credit on all personal auto policies.</div>
  <div class="abs phone">1-800-555-0142, <a>Call Us</a></div>
</div>

<div class="abs brand">
  <div class="mark"></div>
  <div class="name">SUMMIT RIDGE<br>FINANCIAL</div>
</div>
<nav class="abs nav"><span>Home</span><span>About Us</span><span>Insurance</span><span>Testimonials</span><span>Blog</span></nav>
<div class="abs btn quote">Get a quote →</div>

<section class="hero">
  <div class="abs hero-bg"></div>
  <div class="abs hero-photo" role="img" aria-label="Photo of a smiling older couple reviewing papers with an advisor"></div>
  <svg class="abs play" viewBox="0 0 68 68"><circle cx="34" cy="34" r="31" fill="none" stroke="#0b2a55" stroke-width="4"/><path d="M26 20 L50 34 L26 48 Z" fill="#0b2a55"/></svg>
  <p class="abs tagline">Reliable. <span>Personable. Fast.</span></p>
  <h1 class="abs headline"><span class="lead">Are you healthy enough</span><span class="rest">that you are at risk of outliving your retirement savings?</span></h1>
  <p class="abs hero-copy">Only Veranta company gives you an investment with your life insurance policy at no extra cost.</p>
  <div class="abs btn cta1">Get started →</div>
  <div class="abs btn cta2">
    <svg width="13" height="12" viewBox="0 0 13 12"><path d="M6.5 1C3.2 1 1 3 1 5.3c0 1.2.6 2.3 1.6 3L2 11l2.8-1.6c.5.1 1.1.2 1.7.2 3.3 0 5.5-2 5.5-4.3S9.8 1 6.5 1z" fill="none" stroke="#1c2331"/><circle cx="4.3" cy="5.4" r=".7" fill="#1c2331"/><circle cx="6.5" cy="5.4" r=".7" fill="#1c2331"/><circle cx="8.7" cy="5.4" r=".7" fill="#1c2331"/></svg>
    Contact us today</div>
  <div class="abs rating"><span class="stars">★★★★★</span><span>Veranta rated 4.8/5</span></div>
</section>

<div class="abs card c1">
  <div class="img" role="img" aria-label="Photo of an advisor in a suit leaning over a desk" style="background:linear-gradient(160deg,#e6e8ec,#9aa0ab)"></div>
  <div class="icon"><svg width="26" height="26" viewBox="0 0 26 26" fill="none" stroke="#fff" stroke-width="2.4"><circle cx="13" cy="13" r="10.5"/><circle cx="13" cy="13" r="4.5"/><path d="M5.6 5.6l4.2 4.2M20.4 5.6l-4.2 4.2M5.6 20.4l4.2-4.2M20.4 20.4l-4.2-4.2"/></svg></div>
</div>
<div class="abs card c2">
  <div class="img" role="img" aria-label="Photo of an agent on the phone taking notes" style="background:linear-gradient(160deg,#eceef1,#a4aab4)"></div>
  <div class="icon"><svg width="26" height="26" viewBox="0 0 26 26" fill="none" stroke="#fff" stroke-width="2.4"><circle cx="12" cy="14" r="10"/><circle cx="12" cy="14" r="5"/><path d="M12 14L22 4M18 4h4v4"/></svg></div>
</div>
<div class="abs card c3">
  <div class="img" role="img" aria-label="Photo of an agent helping an older client at a table" style="background:linear-gradient(160deg,#e1e4e9,#8d95a2)"></div>
  <div class="icon" style="background:linear-gradient(180deg,#1496e6,#0a67d0)"><svg width="26" height="24" viewBox="0 0 26 24" fill="#fff"><path d="M13 1L1 7h24z"/><rect x="1" y="8" width="24" height="2"/><rect x="4" y="11" width="3" height="8"/><rect x="11.5" y="11" width="3" height="8"/><rect x="19" y="11" width="3" height="8"/><rect x="1" y="20" width="24" height="3"/></svg></div>
  <div class="panel">
    <h3>Guidance from our office agents</h3>
    <p>Understanding your options is an important step. Let agents help guide.</p>
    <div class="link">Get started <span>→</span></div>
  </div>
</div>

<section class="savings">
  <div class="abs rule"></div>
  <h2 class="abs savings-title"><b>How much</b> is your estimated tax savings?</h2>
  <p class="abs intro">Lorem ipsum dolor sit amet, consectetur adipiscing elit, sed do eiusmod tempor incididunt ut labore et dolore magna aliqua. Quis suspendisse ultrices gravida. modo viverra maecenas accumsan lacus vel facilisis.</p>

  <div class="abs feature f1">
    <svg class="ico" viewBox="0 0 32 34"><path d="M6 10l10-7 10 7z" fill="#8fc3f3"/><rect x="2" y="11" width="28" height="18" rx="3" fill="#1d7fe0"/><circle cx="16" cy="20" r="5.5" fill="#fff"/><text x="16" y="23" font-size="8" text-anchor="middle" fill="#1d7fe0" font-family="Rubik" font-weight="700">$</text></svg>
    <h4>Pay Bills</h4>
    <p>Paying those high insurance rates every month can't be very easy.</p>
  </div>
  <div class="abs feature f2">
    <svg class="ico" viewBox="0 0 32 34"><path d="M16 2l12 5v9c0 8-6 13-12 16C10 29 4 24 4 16V7z" fill="#1d7fe0"/><text x="16" y="23" font-size="15" text-anchor="middle" fill="#fff" font-family="Rubik" font-weight="700">$</text></svg>
    <h4>Wealth Protection</h4>
    <p>We work with top insurance companies to ensure you get the best coverage</p>
  </div>
  <div class="abs feature f3">
    <svg class="ico" viewBox="0 0 32 34"><rect x="4" y="1" width="24" height="5" rx="1" fill="#1d7fe0"/><path d="M7 7h18v22a3 3 0 0 1-3 3H10a3 3 0 0 1-3-3z" fill="#9fcbf5"/><circle cx="12" cy="27" r="3.5" fill="#1d7fe0"/><circle cx="20" cy="27" r="3.5" fill="#1d7fe0"/><rect x="12" y="12" width="8" height="10" rx="1" fill="#1d7fe0"/></svg>
    <h4>Protect Income</h4>
    <p>Disability insurance can help pay the bills if a serious keeps you from working.</p>
  </div>
  <div class="abs btn services">Our services →</div>

  <svg class="abs frame" viewBox="0 0 332 325">
    <defs>
      <linearGradient id="ring" x1="0" y1="0" x2="1" y2="1"><stop offset="0" stop-color="#4fd0ff"/><stop offset=".5" stop-color="#1a8ee8"/><stop offset="1" stop-color="#0a5fc9"/></linearGradient>
      <linearGradient id="inner" x1="0" y1="0" x2="1" y2="1"><stop offset="0" stop-color="#e9ecf0"/><stop offset="1" stop-color="#9ba3b0"/></linearGradient>
    </defs>
    <path d="M40 50 Q10 60 5 100 Q0 150 60 240 Q120 320 190 322 Q230 322 255 290 Q300 230 320 110 Q330 40 300 20 Q270 5 200 12 Q100 25 40 50 Z" fill="url(#ring)"/>
    <path d="M48 70 Q25 82 22 110 Q20 150 72 228 Q125 300 185 302 Q220 302 240 275 Q280 220 298 115 Q304 60 282 45 Q258 30 200 34 Q110 45 48 70 Z" fill="#fff" opacity=".35"/>
    <path d="M62 82 Q42 94 40 118 Q38 152 85 222 Q132 286 183 287 Q212 287 229 264 Q264 214 280 120 Q285 74 266 62 Q245 50 198 53 Q118 62 62 82 Z" fill="url(#inner)" role="img" aria-label="Photo of a senior doctor writing notes at his desk"/>
    <path d="M49 2 Q40 0 33 12 L4 100 Q0 116 16 122 Q48 134 80 140 Q100 142 108 130 L150 70 Q155 58 145 50 Q100 15 49 2 Z" fill="#06163a"/>
    <text x="55" y="66" font-family="Rubik" font-weight="700" font-size="33" fill="#1ea8f0" text-anchor="middle">9</text>
    <text x="55" y="88" font-family="Mulish" font-size="11" fill="#fff" text-anchor="middle">Years</text>
    <text x="55" y="104" font-family="Mulish" font-size="11" fill="#fff" text-anchor="middle">Experiences</text>
  </svg>
</section>

</body>
</html>
```